New business! Essential Oils Label for 10 mL Essential Oils Bottles

I need a label design for my new essential oils business. The design should be easily transferable between products. Content should include:
label size W x H 1.25 x 2.875

LAVENDER
Lavandula angustifolia
VOLMIRAâ„¢
100% PURE ESSENTIAL OIL
Net 10 mL
For promotions and additional product information visit fb.com/VolmiraOils
VolmiraOils.com
Boca Raton, FL 33871
888-555-KIPO (5476)
Indications: Massage (10 drops of carrier oil for every drop of essential oil), Bath (10 drops of essential oil) or Inhalation (2-4 drops essential of on a tissue).
EXTERNAL USE ONLY- DILUTE BEFORE APPLICATION
Caution: Do not ingest the oil. Sensitive skin may be irritated by topical use. Avoid contact with eyes. Consult your healthcare practitioner before use. Store oil away from children and pets. Not meant for use during pregnancy. Seek medical care immediately if adverse reaction is experienced.

Target Market(s)

ONLINE SHOPPERS

Industry/Entity Type

Business

Font styles to use
Serif
Sans Serif

Colors

Designer to choose colors to be used in the design.

Requirements
Must have
• CONTENT AS LISTED IN PROJECT DESCRIPTION, LOGO (ATTACHED)
Nice to have
• Files with easily transferable content so the same label design can be used for multiple products.
Should not have
• Too small of print, difficult to read

```html
<!DOCTYPE html>
<html lang="en">
<head>
<meta charset="utf-8">
<title>Volmira Lavender Label – Design One</title>
<link rel="stylesheet" href="https://fonts.googleapis.com/css2?family=Courier+Prime:ital,wght@0,400;0,700;1,700&family=Oranienbaum&family=Rokkitt:wght@500&family=Cinzel:wght@400&family=Arimo:wght@400;700&display=swap">
<style>
  :root {
    --ink: #000000;
    --paper: #ffffff;
    --leaf: #3f7f2e;
    --brand-grey: #333333;
    --lavender-deep: #6a4f9c;
    --lavender-light: #b9a6d8;
    --stem: #7f9a5a;
  }
  * { margin: 0; padding: 0; box-sizing: border-box; }
  html, body { width: 1200px; height: 667px; overflow: hidden; background: var(--paper); }
  .canvas { position: relative; width: 1200px; height: 667px; background: var(--paper); }

  .panel { position: absolute; top: 152px; width: 160px; }
  .panel--front { left: 312px; }
  .panel--back { left: 501px; }

  .black-band { background: var(--ink); color: var(--paper); text-align: center; white-space: nowrap; overflow: hidden; }

  .purity {
    height: 64px; padding-top: 9px;
    font-family: "Courier Prime", monospace; font-size: 16px; line-height: 22px;
  }
  .botanical-art {
    height: 111px;
    background: radial-gradient(ellipse at 45% 45%, var(--lavender-deep) 0%, var(--lavender-light) 45%, rgba(185,166,216,0.25) 70%, var(--paper) 85%),
                linear-gradient(160deg, var(--paper) 0%, var(--stem) 100%);
  }
  .product-name {
    height: 47px; margin-top: 1px;
    font-family: "Rokkitt", serif; font-weight: 500; font-size: 32px; line-height: 47px;
  }
  .latin-block { height: 80px; margin-top: 4px; padding-top: 10px; }
  .latin-name {
    font-family: "Courier Prime", monospace; font-style: italic; font-weight: 700;
    font-size: 13.5px; line-height: 15px; text-transform: uppercase; letter-spacing: 1px;
  }
  .net-volume {
    margin-top: 14px;
    font-family: "Courier Prime", monospace; font-weight: 700; font-size: 9px; text-transform: uppercase; letter-spacing: 0.5px;
  }
  .brand-name {
    margin-top: 24px; text-align: center;
    font-family: "Arimo", sans-serif; font-weight: 400; font-size: 17px; letter-spacing: 2px; color: var(--brand-grey);
  }

  .section-head {
    font-family: "Oranienbaum", serif; font-weight: 400; text-align: center;
  }
  .head-indications { height: 43px; font-size: 31px; line-height: 44px; letter-spacing: -0.6px; }
  .head-caution { height: 40px; margin-top: 10px; font-size: 33px; line-height: 41px; letter-spacing: 2px; }
  .body-copy {
    font-family: "Courier Prime", monospace; font-weight: 700; font-size: 10px; line-height: 13.5px;
    letter-spacing: 0.4px; text-transform: uppercase; color: var(--ink); white-space: nowrap;
  }
  .body-copy--indications { margin-top: 8px; }
  .body-copy--caution { margin-top: 2px; }
  .use-label { text-decoration: underline; }

  .contact {
    position: relative; margin-top: 14px; padding-right: 26px; text-align: center;
    font-family: "Arimo", sans-serif; font-size: 10.5px; line-height: 13px; color: var(--leaf);
  }
  .contact-mark {
    position: absolute; right: 4px; top: 8px; width: 20px; height: 20px; border-radius: 50%; background: var(--leaf);
  }

  .presentation-title {
    position: absolute; left: 724px; top: 264px;
    font-family: "Cinzel", serif; font-weight: 400; font-size: 54px; letter-spacing: 1px; color: var(--ink);
    text-shadow: 3px 5px 6px rgba(0,0,0,0.35);
  }
</style>
</head>
<body>
<main class="canvas">
  <section class="panel panel--front">
    <div class="black-band purity">100% PURE<br>ESSENTIAL OIL</div>
    <div class="botanical-art" role="img" aria-label="Bundle of lavender flower sprigs"></div>
    <div class="black-band product-name">Lavender</div>
    <div class="black-band latin-block">
      <p class="latin-name">Lavandula<br>angustifolia</p>
      <p class="net-volume">net 10 mL</p>
    </div>
    <p class="brand-name">VOLMIRA</p>
  </section>

  <section class="panel panel--back">
    <h2 class="black-band section-head head-indications">INDICATIONS</h2>
    <p class="body-copy body-copy--indications">
      <span class="use-label">Massage:</span> 10 drops of<br>
      carrier oil per drop of<br>
      essential oil<br>
      <span class="use-label">Bath:</span> 10 drops<br>
      <span class="use-label">Inhalation:</span> 2 to 4 drops<br>
      essential oil on cotton<br>
      or tissue
    </p>
    <h2 class="black-band section-head head-caution">CAUTION</h2>
    <p class="body-copy body-copy--caution">
      May irritate sensitive<br>
      skin. Avoid contact with<br>
      eyes.Consult your<br>
      healthcare practitioner<br>
      before using. Store away<br>
      from children and pets.<br>
      Not for use during<br>
      pregnancy. For external<br>
      use only.
    </p>
    <div class="contact">
      www.VolmiraOils.com<br>
      Boca Raton, FL 33871<br>
      888-555-KIPO (5476)
      <span class="contact-mark"></span>
    </div>
  </section>

  <h1 class="presentation-title">DESIGN ONE</h1>
</main>
</body>
</html>
```